Sign Design for Truck Repair Shop center

Need a road-side sign for a pickup truck repair shop called HaulPoint Garage. The logo is attached and should be used on the sign. The background should be white and the main part of the logo should take up a large part of the sign so it can be easily read by passing traffic. The sign is 4 feet tall by 8 feet wide. Also need to add the website address" "www.HaulPointGarage-example.com" and "Call/Text 555.382.4607"

```html
<!DOCTYPE html>
<html lang="en">
<head>
<meta charset="utf-8">
<title>HaulPoint Garage – Road Sign</title>
<link href="https://fonts.googleapis.com/css2?family=Montserrat:wght@500;700;800&display=swap" rel="stylesheet">
<style>
  :root {
    --backdrop: #e9ecef;
    --sign-white: #ffffff;
    --brand-blue: #1656a8;
    --number-gray: #7b7e82;
    --rule-gray: #b9bcc0;
  }
  * { margin: 0; padding: 0; box-sizing: border-box; }
  html, body {
    width: 1200px;
    height: 799px;
    overflow: hidden;
    background: var(--backdrop);
    font-family: "Montserrat", Arial, sans-serif;
  }
  .sign {
    position: absolute;
    left: 40px;
    top: 119px;
    width: 1120px;
    height: 560px;
    background: var(--sign-white);
    overflow: hidden;
    box-shadow: 0 4px 18px rgba(0,0,0,0.12);
  }
  .call {
    position: absolute;
    left: 34px;
    top: 50px;
    display: flex;
    align-items: center;
    gap: 32px;
  }
  .call__icon {
    width: 72px;
    height: 150px;
    background: var(--brand-blue);
    display: flex;
    align-items: center;
    justify-content: center;
    flex: none;
  }
  .call__text {
    display: flex;
    flex-direction: column;
  }
  .call__label {
    font-weight: 700;
    font-size: 30px;
    line-height: 1;
    color: var(--brand-blue);
    text-transform: uppercase;
    letter-spacing: 4px;
    margin-bottom: 10px;
  }
  .call__number {
    font-weight: 800;
    font-size: 112px;
    line-height: 1;
    color: var(--number-gray);
    letter-spacing: 1px;
    white-space: nowrap;
  }
  .sign__rule {
    position: absolute;
    left: 0;
    right: 0;
    height: 4px;
    background: var(--rule-gray);
  }
  .sign__rule--top { top: 250px; }
  .sign__rule--bottom { top: 448px; }
  .brand-name {
    position: absolute;
    left: 0;
    right: 0;
    top: 300px;
    text-align: center;
    font-weight: 800;
    font-size: 88px;
    line-height: 1;
    color: var(--brand-blue);
    text-transform: uppercase;
    letter-spacing: 2px;
    white-space: nowrap;
  }
  .web {
    position: absolute;
    left: 0;
    right: 0;
    top: 482px;
    text-align: center;
    font-weight: 500;
    font-size: 27px;
    line-height: 1.2;
    color: var(--brand-blue);
    letter-spacing: 7px;
    white-space: nowrap;
  }
</style>
</head>
<body>
  <div class="sign">
    <div class="call">
      <div class="call__icon">
        <svg width="48" height="60" viewBox="0 0 48 60" aria-hidden="true">
          <path d="M14 4 L22 16 Q23 19 20 21 L16 24 Q18 34 26 42 L30 39 Q33 37 35 39 L44 48 Q46 51 43 54 L38 57 Q30 60 20 50 Q6 36 4 20 Q3 10 8 6 L11 4 Q13 3 14 4 Z" fill="#ffffff"/>
        </svg>
      </div>
      <div class="call__text">
        <div class="call__label">Call/Text</div>
        <div class="call__number">555.382.4607</div>
      </div>
    </div>

    <div class="sign__rule sign__rule--top"></div>

    <div class="brand-name">HaulPoint Garage</div>

    <div class="sign__rule sign__rule--bottom"></div>

    <div class="web">www.HaulPointGarage-example.com</div>
  </div>
</body>
</html>
```